Independent horror publisher needs new web site

Lantern Quill Books requires a new web site. We are an established independent publisher of horror fiction located in Melbourne, Australia. The publishing industry is undergoing radical changes with the advent of self publication and the new website has to address this issue by attracting future Authors. It needs to be easy to navigate, with a clean, modern style completely devoid of comedic/cheesy stereotypical horror garb. We have had a new logo (attached) designed recently and would like that to used as the main inspiration for the web site. Whilst our current website should not be used as either a practical or stylistic template, feel free to make use of our book covers. (www.lanternquillbooks.example)
Updates
The font on our logo is Brandon Grotesque
Target Market(s)
The target market is authors - as such it cannot be grouped by age, gender, ethinicity etc.
Industry/Entity Type
Industry
Requirements
Must have
- On the front page we need a section where we can post latest news. Links to E-book and Paper stores, Submissions Page, About Us Page, Contact Us Page, forum and games page. Friendwall Like and Chirpline follow buttons.
Should not have
- Cheesy horror themes and fonts.

```html
<!DOCTYPE html>
<html lang="en">
<head>
<meta charset="utf-8">
<title>Submissions — Lantern Quill Books</title>
<link rel="stylesheet" href="https://fonts.googleapis.com/css2?family=Arimo:wght@400;700&family=Josefin+Sans:wght@400&display=swap">
<style>
  :root {
    --canvas: #ffffff;
    --page-light: #e1e8eb;
    --page-dark: #c4d1d4;
    --ink: #3d4144;
    --ink-strong: #2f3336;
    --bar: #46494b;
    --rule: #9fa8ab;
    --link: #3f5360;
  }
  * { box-sizing: border-box; margin: 0; padding: 0; }
  html, body { width: 1200px; height: 900px; overflow: hidden; background: var(--canvas); }
  body { font-family: "Arimo", Arial, sans-serif; color: var(--ink); position: relative; }

  .page {
    position: absolute; left: 108px; top: 0; width: 1038px; height: 900px;
    background: radial-gradient(ellipse 70% 60% at 42% 30%, var(--page-light) 0%, #d6e0e3 55%, var(--page-dark) 100%);
  }
  .top-bar, .bottom-bar { position: absolute; left: 104px; width: 830px; background: var(--bar); }
  .top-bar { top: 0; height: 6px; }
  .bottom-bar { top: 889px; height: 11px; }

  .brand { position: absolute; left: 104px; top: 52px; width: 92px; text-align: center; }
  .brand-disc { width: 90px; height: 90px; border-radius: 50%; background: var(--bar); }
  .brand-name {
    margin-top: 7px; font-family: "Josefin Sans", Arial, sans-serif; font-weight: 400;
    font-size: 8.6px; letter-spacing: 0.2px; white-space: nowrap; color: var(--ink);
  }

  .main-nav { position: absolute; top: 97px; left: 0; width: 100%; }
  .main-nav a {
    position: absolute; font-weight: 700; font-size: 13px; letter-spacing: 0.9px;
    color: var(--ink); text-decoration: none; white-space: nowrap;
  }
  .main-nav a.is-current::before {
    content: ""; position: absolute; left: 50%; top: -20px; width: 6px; height: 6px;
    margin-left: -3px; border-radius: 50%; background: var(--ink);
  }

  .rule { position: absolute; left: 104px; width: 831px; height: 1px; background: var(--rule); }
  .rule--head { top: 193px; }
  .rule--foot { top: 837px; }

  .page-title { position: absolute; left: 104px; top: 224px; font-size: 21px; font-weight: 700; color: var(--ink-strong); }

  .col { position: absolute; width: 405px; font-size: 12.5px; line-height: 18.7px; }
  .col--left { left: 104px; }
  .col--right { left: 534px; }
  .intro { top: 267px; }
  .section { top: 434px; }
  .section h2 { font-size: 17px; font-weight: 400; color: var(--ink-strong); margin-bottom: 12px; letter-spacing: -0.2px; }
  .section p { margin-bottom: 18.7px; }
  .section ul { list-style: none; margin: 0 0 18.7px 10px; }
  .section li::before { content: "• "; }
  a.text-link { color: var(--link); text-decoration: underline; }

  .site-footer { position: absolute; top: 860px; left: 105px; width: 830px; font-size: 12.5px; }
  .copyright { font-weight: 700; font-size: 12.5px; color: var(--ink-strong); }
  .footer-links { position: absolute; right: 2px; top: 0; }
  .footer-links a { color: var(--link); }
  .footer-links .contact { margin-right: 17px; }
</style>
</head>
<body>
  <div class="page">
    <div class="top-bar"></div>

    <header>
      <div class="brand">
        <div class="brand-disc"></div>
        <div class="brand-name">LANTERN QUILL BOOKS</div>
      </div>
      <nav class="main-nav">
        <a href="#" style="left:247px">HOME</a>
        <a href="#" style="left:324px">ABOUT</a>
        <a href="#" style="left:408px">STORE</a>
        <a href="#" class="is-current" style="left:490px">SUBMISSIONS</a>
        <a href="#" style="left:623px">FORUMS</a>
        <a href="#" style="left:719px">GAMES</a>
        <a href="#" style="left:804px">CONTACT</a>
      </nav>
    </header>

    <div class="rule rule--head"></div>

    <main>
      <h1 class="page-title">Submissions</h1>

      <p class="col col--left intro">Donec sed tellus eget sapien mollis ornare. In hac habitasse platea dictumst. Sed orci dui, volutpat sit amet eleifend sit amet, fringilla pretium lectus. In sed magna elit. Quisque pretium libero vitae urna lobortis aliquam. Suspendisse et scelerisque mi. Aliquam feugiat tempus tellus, quis sollicitudin arcu luctus in. In eu enim massa. Duis quis lectus et risus volutpat interdum.</p>
      <p class="col col--right intro">Sed vel ipsum enim. Nullam risus magna, sagittis vel pellentesque quis, ultricies in felis. Pellentesque tincidunt, nibh id ultricies mollis, tortor nisl malesuada nisi, in feugiat tortor justo ut lorem. Suspendisse potenti. Curabitur quis neque id nisl vestibulum ornare id eget ante. Nunc volutpat quam eget diam egestas imperdiet.</p>

      <section class="col col--left section">
        <h2>NOVELS</h2>
        <p>Lantern Quill Books is now OPEN for NOVEL submissions.</p>
        <p>Lantern Quill Books is currently accepting novel submissions in the following categories:</p>
        <ul>
          <li>Survival Horror</li>
          <li>Apocalypse</li>
          <li>Dark Humour</li>
          <li>Sci-Fi Horror</li>
        </ul>
        <p>Due to the high number of submissions we are receiving, novels should be submitted as a query including the first three chapters and a synopsis to <a class="text-link" href="#">novels@lanternquillbooks.example</a> if we are interested in your work we will request the full manuscript within 21 days. Submissions not responded to within this period should be considered a rejection.</p>
      </section>

      <section class="col col--right section">
        <h2>ANTHOLOGIES</h2>
        <p>Please check <a class="text-link" href="#">our forum</a> for open Anthologies:</p>
      </section>
    </main>

    <div class="rule rule--foot"></div>

    <footer class="site-footer">
      <span class="copyright">2012 LANTERN QUILL BOOKS</span>
      <span class="footer-links"><a class="contact" href="#">Contact us</a>Find us on <a href="#">Chirpline</a> and <a href="#">Friendwall</a></span>
    </footer>

    <div class="bottom-bar"></div>
  </div>
</body>
</html>
```